American cannabis tech company business card design

Quillo.com is seeking a modern, professional, and brand-aligned business card that represents our company and its core values: Mission, Story, Values, and Impact. As an innovative cannabis company, we want a business card that is not only visually appealing but also serves as a representation of who we are and what we stand for.

Project Scope: Design a double-sided business card that integrates our brand identity and core values. Incorporate our key brand elements, ensuring a sleek and contemporary aesthetic. Visually reflect our core values (Mission, Story, Values, Impact) in a way that is engaging yet professional.

Target Market(s)

Vendors, third parties,

Contact Information for Business Card

Contact details (name, title, email, phone, website, etc.)

Font styles to use
Other font styles liked:
• Caslon, Centra

Colors

Designer to choose colors to be used in the design.

Requirements
Must have
• Quillo.com logo and branding A creative yet clean way to integrate our core values (Mission, Story, Values, Impact) Modern typography and a well-structured layout
Nice to have
• forest green, grey, white, black
Should not have
• references to marijuana, leafs, plants, or related product

```html
<!DOCTYPE html>
<html lang="en">
<head>
<meta charset="UTF-8">
<title>Quillo Business Card</title>
<link rel="stylesheet" href="https://fonts.googleapis.com/css2?family=Libre+Caslon+Text:wght@700&family=Montserrat:wght@400;800&display=swap">
<style>
  :root {
    --forest: #1b3320;
    --cream: #fbf8f1;
    --paper: #ffffff;
    --ink: #1f1f1f;
    --stage: #3a3a3a;
    --rule: #2c2c2c;
  }
  * { margin: 0; padding: 0; box-sizing: border-box; }
  html, body { width: 1200px; height: 875px; overflow: hidden; }
  body {
    background: var(--stage);
    position: relative;
    font-family: "Montserrat", sans-serif;
  }
  .card {
    position: absolute;
    width: 520px;
    height: 300px;
    border-radius: 22px;
    box-shadow: 0 18px 40px rgba(0,0,0,0.35);
  }
  .card--front {
    left: 60px;
    top: 110px;
    background: var(--forest);
    display: flex;
    align-items: center;
    justify-content: center;
  }
  .wordmark {
    font-family: "Montserrat", sans-serif;
    font-weight: 800;
    letter-spacing: -1px;
    line-height: 1;
  }
  .card--front .wordmark { color: var(--cream); font-size: 104px; }
  .card--back {
    left: 620px;
    top: 465px;
    background: var(--paper);
  }
  .card--back .wordmark {
    position: absolute;
    left: 92px;
    top: 150px;
    color: var(--forest);
    font-size: 40px;
  }
  .divider {
    position: absolute;
    left: 272px;
    top: 62px;
    width: 1.5px;
    height: 156px;
    background: var(--rule);
  }
  .contact {
    position: absolute;
    left: 290px;
    top: 58px;
    color: var(--ink);
  }
  .contact__name {
    font-family: "Libre Caslon Text", serif;
    font-weight: 700;
    font-size: 19px;
    color: var(--forest);
  }
  .contact__title {
    font-family: "Libre Caslon Text", serif;
    font-weight: 700;
    font-size: 9px;
    color: var(--ink);
    margin: 2px 0 12px 16px;
  }
  .contact__line {
    font-size: 12.5px;
    line-height: 1.25;
  }
  .contact__list { list-style: none; margin-top: 8px; }
  .contact__list li {
    display: flex;
    align-items: center;
    gap: 8px;
    font-size: 12.5px;
    line-height: 1.55;
  }
  .contact__list svg { width: 11px; height: 11px; fill: var(--forest); }
</style>
</head>
<body>
  <section class="card card--front" aria-label="Card front">
    <span class="wordmark">Quillo</span>
  </section>

  <section class="card card--back" aria-label="Card back">
    <span class="wordmark">Quillo</span>
    <div class="divider"></div>
    <div class="contact">
      <p class="contact__name">Dana Whitlow</p>
      <p class="contact__title">Owner</p>
      <p class="contact__line">415 Linden Park Ave, #112</p>
      <p class="contact__line">Brookfield, OH 43219</p>
      <ul class="contact__list">
        <li>
          <svg viewBox="0 0 24 24" aria-hidden="true"><path d="M6.6 10.8a15.1 15.1 0 0 0 6.6 6.6l2.2-2.2c.3-.3.7-.4 1-.2 1.1.4 2.3.6 3.6.6.6 0 1 .4 1 1V20c0 .6-.4 1-1 1A17 17 0 0 1 3 4c0-.6.4-1 1-1h3.5c.6 0 1 .4 1 1 0 1.3.2 2.5.6 3.6.1.3 0 .7-.2 1z"/></svg>
          555-318-0247
        </li>
        <li>
          <svg viewBox="0 0 24 24" aria-hidden="true"><path d="M2 5h20v14H2z M2 5l10 8 10-8" /></svg>
          info@quillo.com
        </li>
        <li>
          <svg viewBox="0 0 24 24" aria-hidden="true"><circle cx="12" cy="12" r="10"/></svg>
          www.quillo.com
        </li>
      </ul>
    </div>
  </section>
</body>
</html>
```